CD Cover Design Project

Don't have a huge brief or visual idea of exactly what i want, but here are the details:

Band Name: The Brinewhistles
Title: Most of Where We Ought to Go
Genre: indie rock - think Carried On Lanterns, Drubb, Tarvy, The Plonts, etc)

Definitely want the name and title on the cover. It could be more photography based or design based. A little more abstract. Totally open. Brinewhistles chew up everything they see... One thought was an eaten, old beat up guitar...maybe too cliche.

Album covers i love: Allwhiles, Marble Sleeping, Sidestep the Pebbles, Dusty Ladders, Make me Drift

Happy to send music or give feedback on concepts prior to working on them...not sure of the rules...whatever is within them.

```html
<!DOCTYPE html>
<html lang="en">
<head>
<meta charset="utf-8">
<title>The Brinewhistles — Most of Where We Ought to Go</title>
<link rel="stylesheet" href="https://fonts.googleapis.com/css2?family=Kalam:wght@700&family=Didact+Gothic&display=swap">
<style>
  :root {
    --spine: #0b0806;
    --ember-deep: #7e2208;
    --ember: #c4481a;
    --rust: #a8380f;
    --amber: #e3882a;
    --gold: #f4b84a;
    --sun: #fde7a6;
    --haze: #fbe9c4;
    --band-ink: #8e2522;
    --mark-core: #5a2a22;
    --mark-edge: #7a3a2c;
    --glow: rgba(255, 250, 240, 0.95);
    --strip: rgba(196, 74, 24, 0.72);
    --title-ink: #fff7ec;
  }
  * { margin: 0; padding: 0; box-sizing: border-box; }
  html, body {
    width: 1200px;
    height: 1011px;
    overflow: hidden;
    background: #ffffff;
  }
  .cover {
    position: relative;
    width: 1200px;
    height: 1011px;
    overflow: hidden;
  }
  .cover__spine {
    position: absolute;
    left: 0; top: 0;
    width: 57px; height: 100%;
    background: var(--spine);
  }
  .cover__photo {
    position: absolute;
    left: 57px; top: 0;
    width: 1143px; height: 100%;
    background:
      radial-gradient(circle at 10% 8%, var(--haze) 0, rgba(251,233,196,0.75) 90px, rgba(251,233,196,0) 230px),
      radial-gradient(ellipse 120px 90px at 92% 36%, rgba(253,231,166,0.55) 0, rgba(253,231,166,0) 100%),
      radial-gradient(ellipse 70px 50px at 8% 72%, rgba(253,200,120,0.55) 0, rgba(253,200,120,0) 100%),
      radial-gradient(ellipse 90px 60px at 30% 86%, rgba(250,190,110,0.45) 0, rgba(250,190,110,0) 100%),
      radial-gradient(ellipse 60px 45px at 96% 78%, rgba(253,220,150,0.55) 0, rgba(253,220,150,0) 100%),
      radial-gradient(ellipse 260px 200px at 58% 62%, var(--sun) 0, rgba(253,231,166,0) 100%),
      radial-gradient(ellipse 560px 430px at 60% 48%, var(--gold) 0, var(--amber) 50%, rgba(227,136,42,0) 82%),
      radial-gradient(ellipse 320px 240px at 88% 12%, #e39a4a 0, rgba(227,154,74,0) 100%),
      radial-gradient(ellipse 380px 200px at 20% 70%, var(--rust) 0, rgba(168,56,15,0) 100%),
      linear-gradient(180deg, #c9662a 0%, var(--ember) 45%, var(--ember-deep) 100%);
  }
  .cover__mark {
    position: absolute;
    left: 262px; top: 52px;
    width: 293px; height: 300px;
    border-radius: 46% 46% 50% 50% / 40% 40% 60% 60%;
    background: radial-gradient(ellipse at 50% 45%, var(--mark-edge) 0, var(--mark-core) 70%);
    box-shadow: 0 0 22px 10px var(--glow), 0 0 50px 18px rgba(255,245,230,0.45);
  }
  .cover__band {
    position: absolute;
    left: 60px; top: 370px;
    width: 650px;
    font-family: "Kalam", cursive;
    font-weight: 700;
    font-size: 106px;
    line-height: 122px;
    color: var(--band-ink);
    text-align: center;
    text-shadow:
      0 0 6px var(--glow),
      0 0 14px var(--glow),
      0 0 26px rgba(255,250,240,0.8),
      0 0 44px rgba(255,250,240,0.55);
  }
  .cover__strip {
    position: absolute;
    left: 57px; top: 856px;
    width: 1143px; height: 104px;
    background: var(--strip);
    display: flex;
    align-items: center;
    justify-content: center;
  }
  .cover__title {
    font-family: "Didact Gothic", sans-serif;
    font-size: 42px;
    letter-spacing: 7px;
    text-transform: uppercase;
    color: var(--title-ink);
    white-space: nowrap;
  }
</style>
</head>
<body>
  <main class="cover">
    <div class="cover__spine"></div>
    <div class="cover__photo" role="img" aria-label="Close-up photograph of a golden autumn maple leaf against a blurred orange background of fallen leaves"></div>
    <div class="cover__mark" role="img" aria-label="Band emblem illustration in dark brown with a white glow"></div>
    <h1 class="cover__band">The Brinewhistles</h1>
    <div class="cover__strip">
      <p class="cover__title">Most of Where We Ought to Go</p>
    </div>
  </main>
</body>
</html>
```